Quorvane Learning App for Children with Dyslexia

Project Description:

We are seeking a talented UI/UX designer to create engaging and intuitive designs for Quorvane, an innovative educational app designed to help children learn letters and words through a multisensory learning approach. The app aims to be particularly helpful for children with dyslexia, providing a supportive and interactive learning environment.

Key App Features & Design Requirements:

Account Creation Screen: Design a welcoming and straightforward sign-up page that allows users to register with their email or continue with Brindlewave. The design should be clean, focusing on user-friendliness and accessibility, adhering to our terms of service and privacy policy.

Main Screen Design: The main screen should allocate at least 4/6 of its height to the interactive drawing area. It needs to display word prompts in both correct and scrambled orders and include options to "Show all Words," "Play all words," and a search function. The interface should be vibrant, engaging, and easy to navigate for children.

Profile Section: Create a user-friendly profile page that allows users to edit their profile image, name, username, email, links, and bio. The design should be clean and encourage user engagement.

QuorTally Page: This section will display the user's learning progress, including rankings, a learning curve, and recently learned words. It should visually represent progress in a motivating and understandable way, suitable for a younger audience.

Visual and Auditory Feedback Implementation: Incorporate elements that support visual and auditory feedback, using dyslexia-friendly formats. This includes choosing appropriate colors, fonts, and auditory cues.

Accessibility and Customization Settings: Designs should include settings for adjusting visual contrast, font size, and the word list to accommodate individual preferences and needs.

Feel free to add more interactions and/or pages.

Design preferences:

Color Scheme: Use a bright, inviting color palette that stimulates learning and engagement without overwhelming the users.
Font Selection: Opt for fonts that are readable and accessible, particularly for users with dyslexia.
Icons and Graphics: Design custom icons and graphics that are cohesive with the app's theme and purpose. Illustrations should be simple, relatable, and supportive of the learning process.

Target Market(s)

Educational

Industry/Entity Type

Educational

Colors
0054AA
0677BA
7BADD7
CADEEF
E8F1F8
0094D4
00A9DD
6FCCEA
C7EBF8
E9F6FB

Requirements
Must have
• Educational app, a writing area, scoring and account management
Nice to have
• Statistics, Ranking Page, Settings and some nice visual features

```html
<!DOCTYPE html>
<html lang="en">
<head>
<meta charset="utf-8">
<title>Quorvane Learning App</title>
<link rel="stylesheet" href="https://fonts.googleapis.com/css2?family=Fredoka:wght@400;500;600&family=Nunito:wght@400;600;700;800&display=swap">
<style>
:root{
  --bg:#dde9f2;
  --ink:#1d1d1f;
  --label:#8a8f94;
  --blue:#0b4ca8;
  --blue-dark:#083f8e;
  --sky:#0a96e0;
  --sky-light:#6fccea;
  --yellow:#fcd33a;
  --white:#ffffff;
  --tile-line:#dcdcdc;
  --soft:#fdf3f1;
  --muted:#9aa0a6;
  --line:#6e6e6e;
}
*{box-sizing:border-box;margin:0;padding:0}
html,body{width:1200px;height:2178px;overflow:hidden}
body{background:var(--bg);font-family:"Nunito",sans-serif;color:var(--ink);position:relative}
.board-title{position:absolute;top:66px;left:0;width:1200px;text-align:center;font-family:"Fredoka",sans-serif;font-weight:600;font-size:38px;letter-spacing:.3px}
.board-thanks{position:absolute;top:1960px;left:0;width:1200px;text-align:center;font-family:"Fredoka",sans-serif;font-weight:600;font-size:36px}
.section-label{position:absolute;font-family:"Fredoka",sans-serif;font-weight:500;font-size:22px;color:var(--label)}
.flow{position:absolute;left:0;top:0;width:1200px;height:2178px;z-index:0}
.screen{position:absolute;width:200px;height:430px;overflow:hidden;border-radius:12px;background:var(--soft);box-shadow:0 4px 14px rgba(20,50,90,.12);z-index:1}
.abs{position:absolute}
/* app bar */
.appbar{position:absolute;left:0;top:0;width:100%;height:36px;background:var(--blue);display:flex;align-items:center;padding:0 9px;color:var(--white);font-weight:700;font-size:8.5px}
.appbar .title-center{position:absolute;left:0;right:0;text-align:center}
.menu-dot{width:14px;height:14px;border-radius:50%;background:var(--yellow);margin-right:8px;display:flex;flex-direction:column;justify-content:center;align-items:center;gap:1.3px;position:relative;z-index:1}
.menu-dot i{display:block;width:6px;height:1px;background:#8a6d00}
.points{margin-left:auto;background:var(--white);color:var(--blue);font-size:6.5px;font-weight:700;border-radius:4px;padding:3px 5px;display:flex;align-items:center;gap:3px}
.points b{width:7px;height:7px;border-radius:50%;border:1.5px solid var(--blue)}
.play-bg{position:absolute;left:0;top:36px;width:100%;bottom:0;background:linear-gradient(135deg,#fdeeee 0%,#fdf6ea 55%,#fdf8df 100%)}
.speaker{position:absolute;right:10px;top:54px;width:20px;height:18px;border-radius:4px;background:#e9e9ee;display:flex;align-items:center;justify-content:center}
.monkey{position:absolute;border-radius:45% 45% 40% 40%;background:radial-gradient(circle at 50% 35%,#e8b679 0%,#b4713a 55%,#8a4f22 100%)}
.answer-box{position:absolute;left:36px;top:183px;width:128px;height:28px;background:var(--white);border-radius:4px;border:1px solid #eee}
.toolbar{position:absolute;display:flex;gap:7px;align-items:center}
.btn-dark,.btn-sky{height:22px;border-radius:3px;font-size:6.5px;font-weight:600;color:var(--white);display:flex;align-items:center;justify-content:center;padding:0 6px}
.btn-dark{background:#1a1a1a}
.btn-sky{background:var(--sky)}
.btn-search{width:23px;height:22px;border-radius:3px;background:var(--yellow);display:flex;align-items:center;justify-content:center}
.word{position:absolute;width:80px;height:30px;background:var(--white);border:1px solid var(--tile-line);border-radius:5px;box-shadow:0 2px 0 #e1e1e1;font-family:"Fredoka",sans-serif;font-weight:500;font-size:14px;color:#333;display:flex;align-items:center;justify-content:center}
.primary-btn{position:absolute;height:30px;background:var(--blue);border-radius:4px;box-shadow:0 2px 0 var(--blue-dark);color:var(--white);font-size:6.5px;font-weight:800;letter-spacing:.5px;display:flex;align-items:center;justify-content:center}
/* sign up */
.signup{background:var(--blue)}
.signup .parrot{left:88px;top:12px;width:24px;height:32px;border-radius:40%;background:linear-gradient(160deg,#e8342b,#ff9b2e)}
.brand{left:0;top:48px;width:200px;text-align:center;font-family:"Fredoka",sans-serif;font-weight:600;font-size:20px;color:var(--yellow);letter-spacing:.5px}
.signup .t{left:0;width:200px;text-align:center;color:var(--white)}
.field{position:absolute;left:17px;width:166px;height:29px;background:var(--white);border-radius:4px;display:flex;align-items:center;padding:0 9px;gap:6px;font-size:6.5px;color:#999;box-shadow:0 2px 0 #8fb0dd}
.outline-btn{position:absolute;left:17px;top:209px;width:166px;height:28px;border:1.5px solid #c9dcf3;border-radius:4px;color:var(--white);font-size:6.5px;font-weight:800;letter-spacing:1px;display:flex;align-items:center;justify-content:center}
.scene-art{left:0;top:352px;width:200px;height:78px;background:linear-gradient(180deg,#3d8ad6 0%,#6cbf3b 45%,#3f9b2a 100%)}
/* letters */
.slot{position:absolute;top:185px;width:25px;height:28px;border-radius:4px;background:#e6e6e9}
.letter{position:absolute;width:29px;height:28px;background:var(--white);border:1px solid var(--tile-line);border-radius:4px;box-shadow:0 2px 0 #e0e0e0;font-family:"Fredoka",sans-serif;font-weight:600;font-size:15px;color:#333;display:flex;align-items:center;justify-content:center}
.letter.pressed{background:#cfcfd2;color:#555}
/* profile */
.card{position:absolute;background:var(--white);border-radius:6px;box-shadow:0 2px 8px rgba(0,0,0,.06)}
.avatar-photo{background:linear-gradient(160deg,#f7c7cf,#e2536c 60%,#8d2b3e)}
.pfield{position:absolute;left:27px;width:144px;border:1px solid #e3e3e3;border-radius:4px;padding:5px 8px;font-size:7px;font-weight:700;color:#333;box-shadow:0 1.5px 0 #ececec}
.pfield small{display:block;font-size:5.5px;font-weight:400;color:#b0b0b0;margin-bottom:2px}
.pfield .go{position:absolute;right:7px;top:11px}
.pfield p{font-weight:600;line-height:1.6}
.tag-add{position:absolute;right:5px;top:5px;background:var(--yellow);font-size:4.8px;font-weight:800;padding:1px 4px;border-radius:2px;color:#333}
/* stats */
.tab{position:absolute;top:52px;height:18px;border:1px solid #e0e0e0;border-radius:3px;font-size:6.5px;font-weight:600;display:flex;align-items:center;justify-content:center;background:var(--white)}
.tab.on{background:var(--blue);color:var(--white);border-color:var(--blue)}
.chip{position:absolute;height:17px;border:1px solid #dedede;border-radius:3px;font-size:6.5px;font-weight:600;display:flex;align-items:center;justify-content:center;box-shadow:0 1.5px 0 #ececec}
.trophy{background:linear-gradient(160deg,#ffd15a,#f08a1c)}
/* result */
.dim{position:absolute;inset:0;background:rgba(18,18,22,.78);z-index:5}
.modal{position:absolute;left:14px;top:135px;width:168px;height:157px;background:var(--white);border-radius:4px;z-index:6}
/* ranking */
.ranking{background:var(--blue)}
.rank-tag{left:41px;top:47px;width:93px;height:38px;background:linear-gradient(90deg,#3e7fd0,#5b9de0);border-radius:3px;color:var(--white);font-size:7px;font-weight:800;padding:6px 8px;line-height:1.5}
.crown{width:22px;height:14px;border-radius:3px;background:linear-gradient(180deg,#ffd84a,#e49a16)}
.face{border-radius:50%;border:2px solid var(--white)}
.podium-name{font-size:6px;font-weight:700;text-align:center;width:40px}
.podium-score{width:22px;height:10px;border-radius:3px;background:#e4e7ee;font-size:5.5px;font-weight:700;display:flex;align-items:center;justify-content:center}
.rank-row{position:absolute;left:26px;width:146px;height:27px;background:var(--white);border:1px solid #e6e6e6;border-radius:4px;display:flex;align-items:center;padding:0 5px;gap:5px;font-size:6.5px;font-weight:600;box-shadow:0 1.5px 0 #ececec}
.rank-row .n{width:10px;height:10px;border-radius:50%;background:#eee;font-size:5px;display:flex;align-items:center;justify-content:center}
.rank-row .pic{width:12px;height:12px;border-radius:50%}
.rank-row .s{margin-left:auto;background:#eceef2;border-radius:3px;padding:1px 5px;font-size:5.5px}
</style>
</head>
<body>

<h1 class="board-title">Quorvane Learning App</h1>

<svg class="flow" viewBox="0 0 1200 2178" aria-hidden="true">
  <path d="M581 638 V704 H134 V1571 H161" fill="none" stroke="var(--line)" stroke-width="1.6"/>
  <path d="M156 1567 L163 1571 L156 1575" fill="none" stroke="var(--line)" stroke-width="1.6"/>
</svg>

<!-- Row 1 labels -->
<div class="section-label" style="left:183px;top:178px">01.Main Screen</div>
<div class="section-label" style="left:489px;top:178px">02.Main Screen one</div>
<div class="section-label" style="left:817px;top:178px">03.Main Screen two</div>

<!-- 01 Sign up -->
<section class="screen signup" style="left:178px;top:239px">
  <div class="abs parrot" role="img" aria-label="Red parrot mascot"></div>
  <div class="abs brand">Quorvane</div>
  <div class="abs t" style="top:86px;font-size:7.5px;font-weight:600">Learn letters and words</div>
  <div class="abs t" style="top:128px;font-size:10px;font-weight:700">Create an account</div>
  <div class="abs t" style="top:145px;font-size:6.5px">Enter your email to sign up for this app</div>
  <div class="field" style="top:167px">
    <svg width="9" height="7" viewBox="0 0 9 7"><rect x=".5" y=".5" width="8" height="6" rx="1" fill="none" stroke="#8c6de0"/><path d="M.8 1 4.5 4 8.2 1" fill="none" stroke="#8c6de0"/></svg>
    email@example.com
  </div>
  <div class="outline-btn">SIGN UP WITH EMAIL</div>
  <div class="abs t" style="top:255px;font-size:6.5px;color:#c9dcf3">——— • OR • ———</div>
  <div class="field" style="top:280px;color:#444;font-weight:600">
    <span style="width:8px;height:8px;border-radius:50%;background:#4285f4;display:inline-block"></span>
    Continue With Brindlewave
    <svg style="margin-left:auto" width="9" height="7" viewBox="0 0 9 7"><path d="M0 3.5H8M5 .5 8 3.5 5 6.5" fill="none" stroke="#6a5ae0" stroke-width="1"/></svg>
  </div>
  <div class="abs t" style="top:320px;font-size:6px;line-height:1.9;color:#c9dcf3;padding:0 20px">By clicking continue, you agree to our <b style="color:#fff">Terms of Service</b> and <b style="color:#fff">Privacy Policy</b></div>
  <div class="abs scene-art" role="img" aria-label="Two children playing on a green meadow with letter blocks"></div>
</section>

<!-- 02 Main screen one -->
<section class="screen" style="left:489px;top:239px">
  <div class="play-bg"></div>
  <header class="appbar"><span class="menu-dot"><i></i><i></i><i></i></span>Main Screen<span class="points"><b></b>16 Points</span></header>
  <div class="speaker"><svg width="8" height="8" viewBox="0 0 8 8"><path d="M1 3h2l2-2v6L3 5H1z" fill="var(--blue)"/></svg></div>
  <div class="monkey" role="img" aria-label="Cartoon monkey sitting" style="left:58px;top:66px;width:84px;height:100px"></div>
  <div class="answer-box"></div>
  <div class="toolbar" style="left:10px;top:239px"><span class="btn-dark" style="width:70px">Show All Words</span><span class="btn-sky" style="width:70px">Play All Words</span><span class="btn-search"><svg width="9" height="9" viewBox="0 0 9 9"><circle cx="3.8" cy="3.8" r="2.8" fill="none" stroke="#222" stroke-width="1.3"/><path d="M6 6 8.3 8.3" stroke="#222" stroke-width="1.3"/></svg></span></div>
  <div class="word" style="left:13px;top:278px">onmkye</div>
  <div class="word" style="left:108px;top:278px">monkey</div>
  <div class="word" style="left:13px;top:317px">Keymon</div>
  <div class="word" style="left:108px;top:317px">moyekn</div>
  <div class="primary-btn" style="left:10px;top:370px;width:179px">SHOW ME THE RESULTS</div>
</section>

<!-- 03 Main screen two -->
<section class="screen" style="left:824px;top:239px">
  <div class="play-bg"></div>
  <header class="appbar"><span class="menu-dot"><i></i><i></i><i></i></span>Main Screen<span class="points"><b></b>16 Points</span></header>
  <div class="speaker"><svg width="8" height="8" viewBox="0 0 8 8"><path d="M1 3h2l2-2v6L3 5H1z" fill="var(--blue)"/></svg></div>
  <div class="answer-box" style="left:33px;width:146px"></div>
  <div class="toolbar" style="left:10px;top:239px"><span class="btn-dark" style="width:70px">Show All Words</span><span class="btn-sky" style="width:70px">Play All Words</span><span class="btn-search"><svg width="9" height="9" viewBox="0 0 9 9"><circle cx="3.8" cy="3.8" r="2.8" fill="none" stroke="#222" stroke-width="1.3"/><path d="M6 6 8.3 8.3" stroke="#222" stroke-width="1.3"/></svg></span></div>
  <div class="word" style="left:13px;top:278px">onmkye</div>
  <div class="word" style="left:108px;top:278px">monkey</div>
  <div class="word" style="left:13px;top:317px">Keymon</div>
  <div class="word" style="left:108px;top:317px">moyekn</div>
  <div class="primary-btn" style="left:10px;top:370px;width:179px">SHOW ME THE RESULTS</div>
</section>

<!-- Row 2 labels -->
<div class="section-label" style="left:183px;top:744px">04.Main Screen three</div>
<div class="section-label" style="left:483px;top:744px">05.Profile</div>
<div class="section-label" style="left:823px;top:744px">06.Stats</div>

<!-- 04 Main screen three -->
<section class="screen" style="left:190px;top:814px;width:197px;height:428px">
  <div class="play-bg" style="background:var(--soft)"></div>
  <header class="appbar"><span class="menu-dot"><i></i><i></i><i></i></span>Main Screen<span class="points"><b></b>16 Points</span></header>
  <div class="speaker"><svg width="8" height="8" viewBox="0 0 8 8"><path d="M1 3h2l2-2v6L3 5H1z" fill="var(--blue)"/></svg></div>
  <div class="monkey" role="img" aria-label="Cartoon monkey sitting" style="left:57px;top:66px;width:88px;height:102px"></div>
  <div class="letter" style="left:10px;top:185px;width:24px">m</div>
  <div class="slot" style="left:41px"></div><div class="slot" style="left:72px"></div><div class="slot" style="left:103px"></div><div class="slot" style="left:135px"></div><div class="slot" style="left:166px;width:24px"></div>
  <div class="toolbar" style="left:9px;top:240px"><span class="btn-dark" style="width:70px">Show All Words</span><span class="btn-sky" style="width:69px">Play All Words</span><span class="btn-search"><svg width="9" height="9" viewBox="0 0 9 9"><circle cx="3.8" cy="3.8" r="2.8" fill="none" stroke="#222" stroke-width="1.3"/><path d="M6 6 8.3 8.3" stroke="#222" stroke-width="1.3"/></svg></span></div>
  <div class="letter" style="left:12px;top:280px">o</div>
  <div class="letter" style="left:60px;top:280px">n</div>
  <div class="letter pressed" style="left:108px;top:280px">m</div>
  <div class="letter" style="left:156px;top:280px">k</div>
  <div class="letter" style="left:12px;top:323px">y</div>
  <div class="letter" style="left:60px;top:323px">e</div>
  <div class="primary-btn" style="left:9px;top:370px;width:179px">SHOW ME THE RESULTS</div>
</section>

<!-- 05 Profile -->
<section class="screen" style="left:490px;top:814px;width:197px;height:474px">
  <header class="appbar"><span class="menu-dot" style="font-size:8px;color:#8a6d00">‹</span><span class="title-center">Profile</span></header>
  <div class="card" style="left:15px;top:100px;width:167px;height:347px"></div>
  <div class="abs avatar-photo" role="img" aria-label="Profile photo of the learner" style="left:65px;top:58px;width:70px;height:70px;border-radius:50%;border:3px solid #fff"></div>
  <div class="abs" style="left:127px;top:82px;width:11px;height:11px;border-radius:50%;background:var(--blue);border:1.5px solid #fff"></div>
  <div class="pfield" style="top:148px"><small>Name</small>Maren Lowe<svg class="go" width="8" height="6" viewBox="0 0 8 6"><path d="M0 3H7M4.5.5 7 3 4.5 5.5" fill="none" stroke="#888" stroke-width=".8"/></svg></div>
  <div class="pfield" style="top:187px"><small>Username</small>@username<svg class="go" width="8" height="6" viewBox="0 0 8 6"><path d="M0 3H7M4.5.5 7 3 4.5 5.5" fill="none" stroke="#888" stroke-width=".8"/></svg></div>
  <div class="pfield" style="top:226px"><small>Email</small>name@example.com<svg class="go" width="8" height="6" viewBox="0 0 8 6"><path d="M0 3H7M4.5.5 7 3 4.5 5.5" fill="none" stroke="#888" stroke-width=".8"/></svg></div>
  <div class="pfield" style="top:264px;height:46px"><small>Links</small><span class="tag-add">Add Link</span><p>mysite.example<br>mylink.example</p></div>
  <div class="pfield" style="top:320px;height:66px"><small>Bio</small><p style="font-size:6.3px;line-height:1.9;margin-top:6px">Lorem ipsum dolor sit amet, consectetur adipiscing elit, sed do eiusmod tempor incididunt.</p></div>
  <div class="primary-btn" style="left:25px;top:400px;width:147px">LOGOUT</div>
</section>

<!-- 06 Stats -->
<section class="screen" style="left:813px;top:814px;width:196px;height:457px">
  <header class="appbar"><span class="menu-dot"><i></i><i></i><i></i></span><span class="title-center">QuorTally</span><span class="abs avatar-photo" role="img" aria-label="Learner avatar" style="right:9px;top:9px;width:18px;height:18px;border-radius:50%;border:1.5px solid #fff"></span></header>
  <div class="tab on" style="left:8px;width:55px">Ranking</div>
  <div class="tab" style="left:70px;width:72px">Correct Words</div>
  <div class="tab" style="left:150px;width:35px">Todo</div>
  <div class="card" style="left:9px;top:91px;width:129px;height:44px;background:#fff6e6;border:1.5px solid #fbe0b8"></div>
  <div class="abs trophy" role="img" aria-label="Third place trophy" style="left:16px;top:100px;width:24px;height:26px;border-radius:50%"></div>
  <div class="abs" style="left:48px;top:101px;font-size:5.5px;color:#b7a58c">Total Ranking</div>
  <div class="abs" style="left:48px;top:110px;font-size:9px;font-weight:700">3<sup style="font-size:5px">rd</sup> Place of 100</div>
  <div class="card" style="left:150px;top:91px;width:60px;height:44px;border:1.5px solid #eee"></div>
  <div class="abs trophy" role="img" aria-label="Medal" style="left:158px;top:100px;width:18px;height:26px;border-radius:6px"></div>
  <div class="card" style="left:9px;top:156px;width:176px;height:159px;border:1.5px solid #eee"></div>
  <div class="abs" style="left:22px;top:166px;font-size:9px;font-weight:600">Learning curve</div>
  <div class="abs" style="left:22px;top:186px;font-size:5.5px;color:#888">100 Words day</div>
  <div class="abs" style="left:22px;top:208px;font-size:5.5px;color:#888">50 Words day</div>
  <svg class="abs" style="left:21px;top:193px" width="156" height="82" viewBox="0 0 156 82">
    <defs><linearGradient id="curveFill" x1="0" y1="0" x2="0" y2="1"><stop offset="0" stop-color="#7badd7" stop-opacity=".75"/><stop offset="1" stop-color="#e8f1f8" stop-opacity=".3"/></linearGradient></defs>
    <path d="M0 9H156M0 31H156M0 80H156" stroke="#ececec" stroke-width=".7"/>
    <path d="M0 66 C8 56 14 48 20 52 S32 74 38 72 S50 36 60 32 S80 12 92 14 S106 40 116 38 S140 12 154 4 L154 80 L0 80 Z" fill="url(#curveFill)"/>
    <path d="M0 66 C8 56 14 48 20 52 S32 74 38 72 S50 36 60 32 S80 12 92 14 S106 40 116 38 S140 12 154 4" fill="none" stroke="#2f78cf" stroke-width="1.3"/>
    <circle cx="154" cy="4" r="2.6" fill="#2f78cf"/>
  </svg>
  <div class="abs" style="left:20px;top:287px;width:156px;display:flex;justify-content:space-between;font-size:5px;color:#777"><span>NOV 2</span><span>3</span><span>4</span><span>5</span><span>6</span><span>7</span><span>8</span></div>
  <div class="card" style="left:9px;top:333px;width:176px;height:94px;border:1.5px solid #eee"></div>
  <div class="abs" style="left:22px;top:341px;font-size:9px;font-weight:600">Recently learned words</div>
  <div class="chip" style="left:21px;top:367px;width:46px">Monkey</div>
  <div class="chip" style="left:74px;top:367px;width:46px">Correct</div>
  <div class="chip" style="left:127px;top:367px;width:46px">Banana</div>
  <div class="chip" style="left:21px;top:396px;width:49px">Drawing</div>
  <div class="chip" style="left:76px;top:396px;width:47px">Peacock</div>
</section>

<!-- Row 3 labels -->
<div class="section-label" style="left:175px;top:1368px">07.Result screen</div>
<div class="section-label" style="left:501px;top:1368px">08.Ranking Screen</div>

<!-- 07 Result -->
<section class="screen" style="left:183px;top:1421px;width:198px;height:429px">
  <div class="play-bg" style="background:var(--soft)"></div>
  <header class="appbar"><span class="menu-dot"><i></i><i></i><i></i></span>Main Screen<span class="points"><b></b>16 Points</span></header>
  <div class="speaker"><svg width="8" height="8" viewBox="0 0 8 8"><path d="M1 3h2l2-2v6L3 5H1z" fill="var(--blue)"/></svg></div>
  <div class="monkey" role="img" aria-label="Cartoon monkey sitting" style="left:60px;top:66px;width:84px;height:100px"></div>
  <div class="word" style="left:13px;top:278px">onmkye</div>
  <div class="word" style="left:108px;top:278px">monkey</div>
  <div class="word" style="left:13px;top:317px">Keymon</div>
  <div class="word" style="left:108px;top:317px">moyekn</div>
  <div class="primary-btn" style="left:14px;top:369px;width:170px">SHOW ME THE RESULTS</div>
  <div class="dim"></div>
  <div class="modal">
    <div class="abs" style="left:84px;top:-6px;width:12px;height:12px;background:#fff;transform:rotate(45deg)"></div>
    <div class="abs" style="left:9px;top:37px;font-size:7.5px;color:#777;letter-spacing:.3px">Correct Answer is</div>
    <div class="abs" role="img" aria-label="Red parrot mascot" style="left:123px;top:18px;width:28px;height:50px;border-radius:40%;background:linear-gradient(160deg,#e8342b,#ffb52e 60%,#2f7fd6)"></div>
    <div class="abs" style="left:10px;top:51px;width:146px;height:30px;border:1px solid #ddd;border-radius:4px;box-shadow:0 2px 0 #e6e6e6;font-family:'Fredoka',sans-serif;font-weight:500;font-size:14px;display:flex;align-items:center;justify-content:center">monkey</div>
    <div class="primary-btn" style="left:11px;top:92px;width:69px;height:29px">CLOSE</div>
    <div class="primary-btn" style="left:86px;top:92px;width:69px;height:29px;background:var(--sky);box-shadow:0 2px 0 #0677ba">NEXT</div>
  </div>
</section>

<!-- 08 Ranking -->
<section class="screen ranking" style="left:501px;top:1421px;width:198px;height:429px">
  <header class="appbar"><span class="menu-dot" style="font-size:8px;color:#8a6d00">‹</span><span class="title-center">Ranking</span></header>
  <div class="abs rank-tag">Weekly Competition<br>Ranking List</div>
  <div class="abs" role="img" aria-label="Parrot perched on a branch" style="left:140px;top:58px;width:56px;height:48px;border-radius:40%;background:linear-gradient(160deg,#e8342b,#ffb52e 55%,#3aa04a)"></div>
  <div class="abs crown" role="img" aria-label="Gold crown" style="left:89px;top:95px;width:24px;height:16px"></div>
  <div class="abs crown" role="img" aria-label="Gold crown" style="left:27px;top:129px"></div>
  <div class="abs crown" role="img" aria-label="Gold crown" style="left:147px;top:128px"></div>
  <div class="abs face avatar-photo" role="img" aria-label="First place player photo" style="left:83px;top:117px;width:34px;height:34px"></div>
  <div class="abs face" role="img" aria-label="Second place player photo" style="left:22px;top:149px;width:32px;height:32px;background:linear-gradient(160deg,#a8e0b0,#3d9a5a)"></div>
  <div class="abs face" role="img" aria-label="Third place player photo" style="left:142px;top:149px;width:32px;height:32px;background:linear-gradient(160deg,#c7d8f4,#4e77c4)"></div>
  <div class="abs" style="left:9px;top:182px;width:177px;height:40px;background:#e9eef6;border-radius:4px 4px 0 0"></div>
  <div class="abs" style="left:70px;top:152px;width:60px;height:32px;background:#f3f5f9;border-radius:4px 4px 0 0"></div>
  <div class="abs podium-name" style="left:80px;top:159px">Wren</div>
  <div class="abs podium-score" style="left:89px;top:171px">1000</div>
  <div class="abs podium-name" style="left:18px;top:193px">Odell</div>
  <div class="abs podium-score" style="left:27px;top:204px">999</div>
  <div class="abs podium-name" style="left:138px;top:193px">Pascal</div>
  <div class="abs podium-score" style="left:147px;top:204px">999</div>
  <div class="abs" style="left:14px;top:224px;width:167px;height:210px;background:#f4f5f8;border-radius:4px"></div>
  <div class="abs" style="left:91px;top:217px;width:16px;height:16px;background:#f4f5f8;transform:rotate(45deg)"></div>
  <div class="rank-row" style="top:244px"><span class="n">4</span><span class="pic" style="background:#5bb36f"></span>Maren Lowe<span class="s">590</span></div>
  <div class="rank-row" style="top:281px"><span class="n">5</span><span class="pic" style="background:#e2536c"></span>Tova Renn<span class="s">588</span></div>
  <div class="rank-row" style="top:318px"><span class="n">6</span><span class="pic" style="background:#6f96d6"></span>Ilsa Moro<span class="s">588</span></div>
  <div class="rank-row" style="top:355px"><span class="n">4</span><span class="pic" style="background:#5bb36f"></span>Maren Lowe<span class="s">590</span></div>
  <div class="rank-row" style="top:392px"><span class="n">5</span><span class="pic" style="background:#e2536c"></span>Tova Renn<span class="s">588</span></div>
</section>

<p class="board-thanks">Thanks for Watching My work</p>

</body>
</html>
```